Business card design needed

We are a Custom Joinery and specialise in design, Manufacture and Installation of kitchens and cabinetry
We currently have a logo based on the northern star in red and black but are open to something that would look fresh and clean
Updates

Project Deadline Extended
Reason: Need a couple days to go through designs. Finding some designs that are great on front and others great on reverse. I would like to be able to comment and get the total look we are after.

Target Market(s)

30-50 year olds who are looking to renovate

Industry/Entity Type

Business

Contact Information for Business Card

Larchfield Fitouts
ABN 37 418 260 573
Colin Pratley - Cabinetmaker/Designer Licence No. 318570K

Requirements
Nice to have
• Maybe a nice fresh modern kitchen picture

```html
<!DOCTYPE html>
<html lang="en">
<head>
<meta charset="utf-8">
<title>Larchfield Fitouts – Business Card</title>
<link rel="stylesheet" href="https://fonts.googleapis.com/css2?family=Marcellus&display=swap">
<style>
  :root {
    --ink: #141414;
    --paper: #ffffff;
    --accent-red: #d3141c;
    --band: rgba(38, 36, 36, 0.78);
    --photo-dark: #2b2b2d;
    --photo-mid: #8d8a86;
    --photo-light: #e4e1da;
    --photo-red: #c4141a;
    --photo-green: #5f8a3c;
  }
  html, body {
    margin: 0;
    padding: 0;
    overflow: hidden;
    background: #ffffff;
  }
  .card {
    position: relative;
    width: 1200px;
    height: 693px;
    overflow: hidden;
    font-family: "Marcellus", "Optima", sans-serif;
    background: var(--paper);
  }
  .card__photo,
  .card__shapes {
    position: absolute;
    inset: 0;
    width: 1200px;
    height: 693px;
  }
  .contact {
    position: absolute;
    right: 46px;
    top: 508px;
    margin: 0;
    text-align: right;
    color: var(--paper);
    text-transform: uppercase;
    line-height: 1;
  }
  .contact__name {
    display: block;
    font-size: 35px;
    letter-spacing: 1px;
    margin-bottom: 18px;
  }
  .contact__line {
    display: block;
    font-size: 26px;
    letter-spacing: 0.5px;
    margin-bottom: 11px;
  }
  .brand {
    position: absolute;
    left: 52px;
    top: 563px;
    display: flex;
    align-items: center;
    gap: 14px;
  }
  .brand__mark {
    width: 22px;
    height: 22px;
    background: var(--accent-red);
  }
  .brand__name {
    font-size: 33px;
    color: var(--ink);
    text-transform: uppercase;
    letter-spacing: 0.5px;
    line-height: 1;
  }
</style>
</head>
<body>
  <div class="card">
    <svg class="card__photo" viewBox="0 0 1200 693" role="img" aria-label="Photograph of a modern kitchen with glossy red tall cabinets, cream island with black benchtop, red bar stools and a garden window">
      <defs>
        <linearGradient id="kitchen-tones" x1="0" y1="0" x2="1" y2="0">
          <stop offset="0" stop-color="var(--photo-dark)"/>
          <stop offset="0.12" stop-color="var(--photo-green)"/>
          <stop offset="0.42" stop-color="var(--photo-light)"/>
          <stop offset="0.55" stop-color="var(--photo-mid)"/>
          <stop offset="0.62" stop-color="var(--photo-red)"/>
          <stop offset="0.93" stop-color="var(--photo-red)"/>
          <stop offset="1" stop-color="var(--photo-light)"/>
        </linearGradient>
        <linearGradient id="kitchen-floor" x1="0" y1="0" x2="0" y2="1">
          <stop offset="0.45" stop-color="#000" stop-opacity="0"/>
          <stop offset="1" stop-color="#3a3a3a" stop-opacity="0.7"/>
        </linearGradient>
      </defs>
      <rect width="1200" height="693" fill="url(#kitchen-tones)"/>
      <rect width="1200" height="693" fill="url(#kitchen-floor)"/>
    </svg>
    <svg class="card__shapes" viewBox="0 0 1200 693" aria-hidden="true">
      <rect class="shape-band" x="0" y="466" width="1200" height="227" fill="var(--band)"/>
      <polygon class="shape-corner" points="0,359 830,693 0,693" fill="var(--paper)"/>
    </svg>

    <div class="brand">
      <span class="brand__mark"></span>
      <span class="brand__name">Larchfield Fitouts</span>
    </div>

    <p class="contact">
      <span class="contact__name">Colin Pratley</span>
      <span class="contact__line">Cabinetmaker/Designer</span>
      <span class="contact__line">Licence No. 318570K</span>
      <span class="contact__line">ABN 37 418 260 573</span>
    </p>
  </div>
</body>
</html>
```